Volunteer Marketplace Needs New Look - www.Brimsey.org

Brimsey is the first online marketplace that lets you buy or sell volunteered services to raise money for charity. (www.Brimsey.org)

We went into live testing a few months ago to get some feedback and feel we need to redo the design. Some points:

- The current design was developed when a previous logo was being used. We later developed the current logo (which we love) and have never felt it really fit into the design. A design that plays up the logo would be great but not required.

- The circles in the logo represent coins which is a theme we are using in our branding (our business cards are coins). The marketplace offers a new form of currency people can use to give back. We don't feel the design should center around this concept, but a small element would be a nice touch.

We want a design that is engaging and fun - but still professional and credible.
Updates

I just want to thank you all for submitting designs. I have been trying to send feedback to everyone and am starting to eliminate designs so I can begin to narrow it. It is so hard to decide. You all did a great job! 

Target Market(s)

There are three target audiences - volunteers donating their services, customers buying donated services, and charities joining the program.

Industry/Entity Type

Business

Requirements
Must have
• - We feel we need to represent on the home page the concept of there being two parties that are coming together - the Volunteer and the Customer.

- We have a 60 second overview video in the works that we would like displayed on the home page.
Nice to have
• Incase it is helpful, here are some designs we like - but please know we are looking for creative ideas. Your design does not have to look like these.

http://www.lendora.org/
https://www.taskwell.com/
http://www.layoutbarn.com/website-templates/40056.html
http://www.layoutbarn.com/website-templates/40121.html
http://www.craftpool.com/

Also - please be creative about what content we put on our home page. We want to modernize the site. We can feed in our blog, twitter, facebook, etc into the home page if you think we should. We need your expertise to recommend what we need to showcase.
Should not have
• Please note that the paragraphs of content do not have to be on the home page. These are there now, but feedback tells us it is too boring - and they is why we are having the video done. So - you do not have to make room for all that text.

```html
<!DOCTYPE html>
<html lang="en">
<head>
<meta charset="utf-8">
<title>Brimsey – The new way to give</title>
<link rel="stylesheet" href="https://fonts.googleapis.com/css2?family=Arimo:wght@400;700&family=Archivo+Black&display=swap">
<style>
:root{
  --page-green:#c6dd63;
  --slate:#56606e;
  --teal:#14a89c;
  --teal-deep:#2c8590;
  --sky:#3d8aa8;
  --white:#ffffff;
  --text:#4a5563;
  --charity-red:#c8101a;
  --link-yellow:#f2e85a;
  --edge:#7fbf3a;
}
*{box-sizing:border-box;margin:0;padding:0}
html,body{width:1200px;height:1000px;overflow:hidden}
body{background:var(--page-green);font-family:"Arimo",Arial,sans-serif;position:relative}
.site{position:absolute;left:130px;top:0;width:928px;height:1000px}

/* header */
.masthead{position:absolute;left:0;top:0;width:928px;height:262px;background:var(--white);overflow:hidden;border-left:1px solid #333;border-right:1px solid #333}
.masthead-art{position:absolute;left:0;top:0}
.brand{position:absolute;left:30px;top:22px;width:310px}
.brand-name{display:flex;align-items:center;gap:14px;font-size:66px;font-weight:700;color:var(--teal-deep);letter-spacing:1px;line-height:1}
.brand-dot{width:38px;height:38px;border-radius:50%;background:#8cc43f;flex:none}
.brand-tagline{margin-top:18px;margin-left:94px;font-size:24px;color:var(--slate)}
.account-bar{position:absolute;left:648px;top:0;width:265px;height:30px;background:var(--slate);border-radius:0 0 8px 8px;color:var(--white);font-size:11px;display:flex;align-items:center;justify-content:space-between;padding:0 10px}
.account-bar a{color:var(--white);text-decoration:none}
.intro{position:absolute;left:406px;top:52px;width:500px;color:var(--white);font-size:12px;line-height:14px}
.intro p{margin-bottom:14px}
.intro a{color:var(--link-yellow)}
.talent-search{display:flex;align-items:center;gap:6px;margin-top:-14px}
.talent-search input{width:232px;height:22px;border:1px solid #999;background:#fff}
.talent-search button{width:84px;height:22px;margin-left:-7px;background:var(--slate);color:#fff;border:0;font-family:inherit;font-size:12px}
.nav-tab{position:absolute;top:196px;display:flex;align-items:center;gap:12px;color:var(--white);font-size:20px;line-height:24px}
.nav-tab svg{flex:none}

/* feature band */
.share{position:absolute;left:751px;top:272px;display:flex;align-items:center;gap:9px;font-size:11px;color:#333}
.share-icon{width:19px;height:19px;border-radius:3px}
.illustration{position:absolute;left:0;top:386px;width:278px;height:188px;background:linear-gradient(#d6e78a,#c6dd63);}
.bubble{position:absolute;left:25px;top:298px;width:228px;height:75px;background:var(--teal);border-radius:14px;color:var(--white);font-size:16px;line-height:20px;text-align:center;padding-top:18px}
.bubble-tail{position:absolute;left:208px;top:368px}
.video{position:absolute;left:278px;top:282px;width:373px;height:271px;background:var(--slate);display:flex;align-items:center;justify-content:center}
.charity-title{position:absolute;left:676px;top:296px;width:240px;color:var(--charity-red);font-family:"Archivo Black",Arial,sans-serif;text-align:center;text-shadow:2px 2px 2px rgba(0,0,0,.35)}
.charity-title .big{font-size:88px;line-height:88px;letter-spacing:1px}
.charity-title .small{font-size:35px;line-height:34px;margin-top:-8px}
.partners{position:absolute;left:692px;top:420px;display:grid;grid-template-columns:repeat(2,100px);gap:6px 14px}
.partner{display:flex;align-items:center;gap:5px;color:var(--charity-red);font-size:12px;font-weight:700;line-height:13px;height:32px}
.partner-mark{width:28px;height:28px;border-radius:50%;background:var(--charity-red);flex:none}
.join{position:absolute;left:683px;top:509px;width:212px;height:43px;background:var(--slate);border-radius:7px;color:var(--white);font-family:"Archivo Black",Arial,sans-serif;font-size:32px;text-align:center;line-height:43px;text-shadow:1px 1px 2px #000}

/* content */
.content{position:absolute;left:0;top:573px;width:928px;height:427px;background:var(--white);border-top:3px solid var(--edge);border-left:1px solid #333;border-right:1px solid #333}
.concept{position:absolute;left:16px;top:24px;width:606px;color:var(--text);font-size:12px;line-height:23px}
.concept h2{font-size:19px;color:var(--slate);margin-bottom:27px}
.concept p{margin-bottom:24px}
.photo{position:absolute;left:662px;width:242px;box-shadow:4px 4px 4px rgba(0,0,0,.35)}
.photo-kids{top:28px;height:183px;background:linear-gradient(135deg,#f38a2a,#f9b14f 55,#e3d6c4)}
.photo-pair{top:234px;height:176px;background:linear-gradient(160deg,#8dc44a,#b9dc5c 60%,#d94a3a)}
</style>
</head>
<body>
<div class="site">
  <header class="masthead">
    <svg class="masthead-art" width="928" height="262" viewBox="0 0 928 262" aria-hidden="true">
      <path d="M380 0 H928 V262 H460 C400 200 350 120 380 0Z" fill="#14a89c"/>
      <path d="M0 200 C120 140 270 140 330 215 V262 H0Z" fill="#56606e"/>
      <path d="M270 262 C330 170 560 130 660 225 V262Z" fill="#2c8590"/>
      <path d="M590 262 C660 170 860 150 928 190 V262Z" fill="#3d8aa8"/>
    </svg>
    <div class="brand">
      <div class="brand-name"><span class="brand-dot"></span>Brimsey</div>
      <div class="brand-tagline">The new way to give.</div>
    </div>
    <div class="account-bar"><span>Welcome Guest</span><span><a href="#">Log in</a> &nbsp;|&nbsp; <a href="#">Register</a></span></div>
    <div class="intro">
      <p>I want to list my talent! Have a talent you would like to donate to help raise money for those in need? <a href="#">Create My Volunteer Profile »</a></p>
      <p>I want to hire donated talent! Looking for an artist, need a music lesson, searching for a handy man?</p>
      <form class="talent-search"><label>Search donated talent:</label><input type="text"><button type="button">Submit</button></form>
    </div>
    <a class="nav-tab" style="left:51px"><svg width="40" height="40"><circle cx="20" cy="20" r="18" fill="none" stroke="#fff" stroke-width="2.5"/><path d="M15 10 L29 20 L15 30Z" fill="#fff"/></svg><span>Search<br>Donated Services</span></a>
    <a class="nav-tab" style="left:374px"><svg width="40" height="40"><circle cx="20" cy="20" r="18" fill="none" stroke="#fff" stroke-width="2.5"/><path d="M15 10 L29 20 L15 30Z" fill="#fff"/></svg><span>Search<br>Help Wanted Ads</span></a>
    <a class="nav-tab" style="left:698px;top:200px"><svg width="40" height="40"><circle cx="20" cy="20" r="18" fill="none" stroke="#fff" stroke-width="2.5"/><path d="M15 10 L29 20 L15 30Z" fill="#fff"/></svg><span>How It Works</span></a>
  </header>

  <div class="share"><span>Share</span><span class="share-icon" style="background:#2a8a3a"></span><span class="share-icon" style="background:#3b5b98"></span><span class="share-icon" style="background:#3aa0d8"></span><span class="share-icon" style="background:#1a6fa8"></span><span class="share-icon" style="background:#e6e6e6"></span></div>

  <div class="illustration" role="img" aria-label="Two cartoon characters, a volunteer and a customer, waving"></div>
  <div class="bubble">Watch 60 second overview<br>video in the works</div>
  <svg class="bubble-tail" width="24" height="26" aria-hidden="true"><path d="M0 0 H20 L4 24Z" fill="#14a89c"/></svg>

  <div class="video" aria-label="Overview video">
    <svg width="130" height="130" viewBox="0 0 130 130"><circle cx="65" cy="65" r="60" fill="none" stroke="#fff" stroke-width="6"/><path d="M47 32 L100 65 L47 98Z" fill="#fff"/></svg>
  </div>

  <div class="charity-title"><div class="big">HELP</div><div class="small">any Charity!</div></div>
  <div class="partners">
    <div class="partner"><span class="partner-mark"></span>Kindred<br>Aid</div>
    <div class="partner"><span class="partner-mark"></span>Kindred<br>Aid</div>
    <div class="partner"><span class="partner-mark"></span>Kindred<br>Aid</div>
    <div class="partner"><span class="partner-mark"></span>Kindred<br>Aid</div>
  </div>
  <a class="join">Join Us!</a>

  <main class="content">
    <section class="concept">
      <h2>THE CONCEPT...</h2>
      <p>JUST LAUNCHED! Brimsey is hot off the press! Welcome to our first visitors.</p>
      <p>Most people want to make a difference, but getting involved with the cause you care about can be a challenge. That's how Brimsey changes the world of giving!</p>
      <p>Everyone has talents - some professional and some hobbies. Lots of people and companies need people with talent. Brimsey enables those with talent to volunteer their time to those who need to hire people with skills -- while benefiting the charity of your choice.</p>
      <p>Whether you are a landscaper, hairdresser, mechanic, musician, computer programmer, and much more -- if you or your business can perform services people will pay for -- you can volunteer your services for hire and have the payment go to charity.</p>
      <p>Not only can you volunteer your time but by hiring volunteered talent such as babysitters, house cleaners, and more you are spending as you normally would but now you are using your money to change the world!</p>
    </section>
    <div class="photo photo-kids" role="img" aria-label="Photo of children lying on an orange mat around a laptop"></div>
    <div class="photo photo-pair" role="img" aria-label="Photo of two smiling children in a green field"></div>
  </main>
</div>
</body>
</html>
```